Values Statement poster template

We want to develop a poster template for our company policies and statements which promote our company values in our workplaces.
These documents are important in showing our clients, suppliers and employees who we are and what we stand for.
The graphic design will incorporate our company logo, and be bright, uplifting and inspiring, developing a graphic theme that we can utilise for other company documents. The design will graphically illustrate and support our values statement, with colour and modern design.
This values poster will be the first in a series of documents using the same theme.The format will be a4 and a3 portrait
We are an environmental service business specialising in rehabilitation and revegetation

Target Market(s)

Tier one clients in industry, Mining, Construction and agriculture

Font styles to use
Other font styles liked:
• calibri

Requirements
Must have
• Professional , high end feel, able to read clearly on a poster
Nice to have
• graphic design elements, symbols, etc which support the message, that can be carried through to various documents such as quality, environmental, safety policies
A bright theme which ties in with our logo colours.

```html
<!DOCTYPE html>
<html lang="en">
<head>
<meta charset="utf-8">
<title>Our Values – Verdalis</title>
<link href="https://fonts.googleapis.com/css2?family=Montserrat:wght@400;500;700;800;900&display=swap" rel="stylesheet">
<style>
  :root {
    --backdrop: #bdbdbd;
    --paper: #ffffff;
    --leaf: #86c240;
    --water: #00abc9;
    --ember: #f37621;
    --slate: #4f4f4f;
    --slate-soft: #6a6a6a;
    --sun: #fcc314;
    --sky: #3a7bd9;
    --orchid: #d84ce0;
    --forest: #007040;
    --ink-light: #ffffff;
  }
  * { box-sizing: border-box; margin: 0; padding: 0; }
  html, body {
    width: 955px; height: 1200px; overflow: hidden;
    background: var(--backdrop);
    font-family: "Montserrat", Arial, sans-serif;
  }
  .poster {
    position: absolute; left: 53px; top: 0;
    width: 849px; height: 1200px;
    background: var(--paper);
  }
  .card {
    position: absolute;
    border-radius: 16px;
    color: var(--ink-light);
    padding: 20px 20px 0 20px;
    overflow: hidden;
  }
  .card h2 {
    font-weight: 900; font-size: 23px; line-height: 0.98;
    letter-spacing: 0.2px; text-transform: uppercase;
  }
  .card .tagline { font-weight: 800; font-size: 16px; margin-top: 6px; }
  .card .lead { font-weight: 700; font-size: 10px; line-height: 1.22; text-align: justify; }
  .card ul { list-style: none; padding-left: 13px; position: relative; z-index: 1; }
  .card li { font-size: 10px; line-height: 1.0; margin-bottom: 7px; }
  .card p.body { font-size: 10px; line-height: 1.05; position: relative; z-index: 1; }
  .emblem { position: absolute; opacity: 0.25; border-radius: 50%; }

  .card--people { left: 31px; top: 31px; width: 249px; height: 296px; background: var(--leaf); }
  .card--planet { left: 301px; top: 31px; width: 249px; height: 296px; background: var(--water); }
  .card--standard { left: 572px; top: 31px; width: 249px; height: 296px; background: var(--ember); }
  .card--hero { left: 31px; top: 351px; width: 519px; height: 339px; background: var(--slate); padding: 0; }
  .card--safe { left: 572px; top: 351px; width: 249px; height: 339px; background: var(--sun); padding-top: 16px; }
  .card--proud { left: 31px; top: 716px; width: 249px; height: 296px; background: var(--sky); padding-top: 14px; }
  .card--together { left: 301px; top: 716px; width: 249px; height: 296px; background: var(--orchid); padding: 26px 24px 0; }
  .card--giveback { left: 572px; top: 716px; width: 249px; height: 296px; background: var(--forest); padding: 32px 22px 0; }

  .hero-title {
    position: absolute; left: 66px; top: 84px;
    font-weight: 900; font-size: 70px; line-height: 0.98; letter-spacing: 1px;
    z-index: 1;
  }
  .skyline-area {
    position: absolute; left: 81px; bottom: 0; width: 341px; height: 119px;
    border-radius: 8px 8px 0 0;
    background: linear-gradient(180deg, rgba(122,122,122,0.35) 0%, var(--slate-soft) 100%);
  }
  .brand {
    position: absolute; left: 40px; top: 1076px;
    display: flex; align-items: center; gap: 14px;
  }
  .brand-dot { width: 30px; height: 30px; border-radius: 50%; background: var(--leaf); }
  .brand-name { font-weight: 700; font-size: 40px; color: var(--forest); letter-spacing: -0.5px; }
  .footer-band { position: absolute; left: 0; bottom: 0; width: 849px; height: 28px; background: var(--forest); }
</style>
</head>
<body>
<main class="poster">
  <section class="card card--people">
    <h2>We value<br>our people</h2>
    <div class="tagline">above everything else</div>
    <div style="font-weight:700;font-size:11px;margin:14px 0 6px;">WE DEMONSTRATE THIS BY:</div>
    <ul>
      <li>Providing safe, positive, enjoyable workplaces where everyone feels valued and respected</li>
      <li>Providing Careers, not Jobs, we grow together</li>
      <li>Encouraging inclusion, participation and collaboration</li>
      <li>Recognising and rewarding contribution and excellence</li>
      <li>Supporting our people through tough times</li>
    </ul>
    <div class="emblem" role="img" aria-label="Two people forming a heart" style="left:165px;top:210px;width:75px;height:75px;background:#c9e6a3;"></div>
  </section>

  <section class="card card--planet">
    <h2>We do good<br>things</h2>
    <div class="tagline">for the planet</div>
    <p class="body" style="margin-top:16px;">Our products are helping revegetate Australia, which we are tremendously proud of.<br>We minimise our environmental impact in everything we do.</p>
    <div class="emblem" role="img" aria-label="Globe" style="left:149px;top:200px;width:88px;height:88px;background:#7fd6e6;"></div>
  </section>

  <section class="card card--standard">
    <h2>We set the<br>standard</h2>
    <ul style="margin-top:34px;padding-left:5px;">
      <li style="margin-bottom:12px;">We are uncompromising on quality</li>
      <li style="margin-bottom:12px;">We are the best at what we do, and we do what we are best at</li>
      <li style="margin-bottom:12px;">We are always improving</li>
      <li>We are pioneering</li>
    </ul>
    <div class="emblem" role="img" aria-label="Star-shaped person" style="left:160px;top:205px;width:72px;height:72px;background:#f9b98a;opacity:0.5;"></div>
  </section>

  <section class="card card--hero">
    <h1 class="hero-title">OUR<br>VALUES</h1>
    <div class="skyline-area" role="img" aria-label="City skyline illustration"></div>
  </section>

  <section class="card card--safe">
    <h2>Our<br>workplaces<br>are safe</h2>
    <p class="lead" style="margin-top:4px;">There is nothing more important to us than our people going home healthy and safe every day. We won’t accept anything less. We believe safety is a management choice. By providing safe work systems, and education we achieve our daily goal of Zero Harm. At Verdalis we;</p>
    <ul style="margin-top:10px;padding-left:8px;">
      <li style="margin-bottom:6px;">Take the time to make our work areas safe, whatever it takes</li>
      <li style="margin-bottom:6px;">Don’t accept shortcuts</li>
      <li style="margin-bottom:6px;">Look out for each other</li>
      <li style="margin-bottom:6px;">Investigate our incidents and learn from them, we won’t accept repeats</li>
      <li style="margin-bottom:6px;">Are constantly looking for ways to improve the safety of our workplaces.</li>
      <li>Think safe, work safer, go home safe!</li>
    </ul>
    <div class="emblem" role="img" aria-label="Safety shield" style="left:155px;top:245px;width:86px;height:86px;background:#fde08a;"></div>
  </section>

  <section class="card card--proud">
    <h2>We are<br>proud of<br>who we are</h2>
    <p class="lead" style="margin:8px 0 12px;">Our reputation means the world to us. We:</p>
    <ul style="padding-left:9px;">
      <li style="margin-bottom:8px;">Treat everyone with respect and we expect it in return</li>
      <li style="margin-bottom:8px;">Follow the rules</li>
      <li style="margin-bottom:8px;">Do what we say we will do</li>
      <li style="margin-bottom:8px;">Own our mistakes and we fix them</li>
      <li>Are trustworthy and transparent</li>
    </ul>
    <div class="emblem" role="img" aria-label="Award ribbon" style="left:155px;top:210px;width:74px;height:74px;background:#8fb5ec;"></div>
  </section>

  <section class="card card--together">
    <h2>We succeed<br>together</h2>
    <p class="lead" style="margin:14px 0 8px;">We believe in win-win relationships. When our business is profitable everyone benefits, our owners, employees, clients and the community. At Verdalis we:</p>
    <ul style="padding-left:8px;">
      <li style="margin-bottom:7px;">Work as a team, we get it done</li>
      <li style="margin-bottom:7px;">We treat our suppliers and subcontractors like they are part of the team</li>
      <li style="margin-bottom:7px;">Are building on our success,</li>
      <li>Choose to work with employees, customers and suppliers who fit our values</li>
    </ul>
    <div class="emblem" role="img" aria-label="Two people giving a high five" style="left:140px;top:190px;width:90px;height:90px;border-radius:12px;background:#eca0f0;"></div>
  </section>

  <section class="card card--giveback">
    <h2>We give back</h2>
    <p class="body" style="margin-top:18px;font-size:11px;line-height:1.68;font-weight:500;text-align:justify;">We appreciate our success and we give back by supporting our community, and those less fortunate.</p>
    <div class="emblem" role="img" aria-label="Adult and child hands" style="left:145px;top:185px;width:88px;height:88px;background:#4ca97a;"></div>
  </section>

  <div class="brand">
    <span class="brand-dot"></span>
    <span class="brand-name">Verdalis</span>
  </div>
  <div class="footer-band"></div>
</main>
</body>
</html>
```